Studying Effectively To Do List

I am looking to design a new "Study To Do List" for High School students (Ages 15 - 18) . This will be printed as an A4 notepad and so should only be a single A4 page.

The Design will need to be professional and look semi-serious but also be appealing to High school students (Ages 15 - 18) and should NOT be gender specific.

I have attached a word document outlining the structure of the page. The space provided should be large enough that people can write in it comfortably.

The notepad will most likely be printed in black and white but I'm also looking at coloured options - colours should be kept to a minimum.

This will be printed professionally and should also include a 3mm bleed.

The design should also include the business logo (included in the word document)

Target Market(s)

High School students (Ages 15 - 18). Both genders

Industry/Entity Type

Education

Font styles to use
Serif
Sans Serif

Requirements
Must have
• Please see the word document attached.
Should not have
• Too much colour

```html
<!DOCTYPE html>
<html lang="en">
<head>
<meta charset="utf-8">
<title>Brightpath Study To Do List</title>
<link rel="stylesheet" href="https://fonts.googleapis.com/css2?family=Roboto:wght@400;700;900&family=Roboto+Condensed:wght@700&display=swap">
<style>
  :root {
    --canvas: #ededed;
    --paper: #ffffff;
    --sidebar: #4a4a4a;
    --row-tint: #ebebeb;
    --rule: #3a3a3a;
    --ink: #1f1f1f;
  }
  html, body { margin: 0; padding: 0; }
  body {
    width: 1200px; height: 960px; overflow: hidden;
    background: var(--canvas);
    font-family: "Roboto", Arial, sans-serif;
    color: var(--ink);
    position: relative;
  }
  .page {
    position: absolute; top: 118px;
    width: 523px; height: 733px;
    background: var(--paper);
    overflow: hidden;
  }
  .page--colour { left: 50px; --accent: #ff7300; --dark: #1c3147; --logo-ring: #ff7300; }
  .page--mono   { left: 620px; --accent: #a3a3a3; --dark: #2b2b2b; --logo-ring: #8a8a8a; }

  .header-shapes, .footer-shapes { position: absolute; left: 0; width: 523px; }
  .header-shapes { top: 0; height: 48px; }
  .footer-shapes { top: 703px; height: 30px; }
  .fill-accent { fill: var(--accent); }
  .fill-dark { fill: var(--dark); }

  .sidebar { position: absolute; left: 0; top: 48px; width: 24px; bottom: 0; background: var(--sidebar); }

  .date-label {
    position: absolute; left: 24px; top: 20px;
    font-weight: 900; font-size: 15px; letter-spacing: 0.3px; color: #333;
  }
  .date-field {
    position: absolute; left: 80px; top: 18px; width: 170px; height: 22px;
    background: var(--paper); box-shadow: 1px 1px 2px rgba(0,0,0,0.25);
  }

  .brand {
    position: absolute; left: 62px; top: 68px; width: 104px;
    display: flex; flex-direction: column; align-items: center; gap: 8px;
  }
  .brand-dot { width: 46px; height: 46px; border-radius: 50%; background: var(--logo-ring); }
  .brand-name { font-weight: 900; font-size: 17px; color: var(--dark); }

  .tab {
    position: absolute; background: var(--dark); color: #fff;
    font-weight: 700; font-size: 7px; letter-spacing: 0.2px;
    padding: 0 3px; line-height: 11px;
  }
  .box { position: absolute; border: 1px solid var(--rule); box-sizing: border-box; background: transparent; }

  .revision-tab { left: 207px; top: 66px; width: 51px; height: 13px; line-height: 13px; padding-left: 6px; }
  .revision { left: 207px; top: 79px; width: 285px; height: 75px; display: grid; grid-template-columns: 1fr 1fr; }
  .revision-col { display: flex; flex-direction: column; }
  .revision-row { flex: 1; display: flex; }
  .revision-row:nth-child(even) { background: var(--row-tint); }
  .num-cell {
    width: 16px; background: var(--dark); color: #fff;
    font-size: 7px; font-weight: 700; display: flex; align-items: center; padding-left: 5px; box-sizing: border-box;
  }

  .homework-tab { left: 47px; top: 179px; height: 11px; }
  .homework { left: 47px; top: 190px; width: 445px; height: 204px; display: flex; flex-direction: column; }
  .line-row {
    flex: 1; font-size: 7px; display: flex; align-items: center; padding-left: 3px;
  }
  .homework .line-row:nth-child(odd) { background: var(--row-tint); }

  .assess-tab { left: 47px; top: 406px; height: 10px; line-height: 10px; }
  .assessments { left: 47px; top: 416px; width: 445px; height: 162px; display: flex; flex-direction: column; }
  .assess-item { flex: 1; display: flex; flex-direction: column; border-bottom: 1px solid var(--rule); }
  .assess-item:last-child { border-bottom: 0; }
  .assess-item .line-row { position: relative; }
  .due-label { position: absolute; left: 275px; font-weight: 700; }
  .due-label::after { content: ""; display: inline-block; width: 22px; }

  .lists { left: 47px; top: 591px; width: 445px; height: 98px; display: grid; grid-template-columns: 223px 1fr; }
  .list { display: flex; flex-direction: column; }
  .list + .list { border-left: 1px solid var(--rule); }
  .list-head {
    height: 21px; background: var(--dark); color: #fff;
    font-size: 7px; font-weight: 700; display: flex; align-items: center; justify-content: center;
  }
  .list-body { flex: 1; display: grid; }
  .list-body--split { grid-template-columns: 1fr 1fr; }
  .list-col { display: flex; flex-direction: column; }
  .list-row { flex: 1; display: flex; border-top: 1px solid var(--rule); }
  .list-row:first-child { border-top: 0; }
  .list-num {
    width: 18px; background: var(--row-tint); font-size: 7px;
    display: flex; align-items: center; padding-left: 6px; box-sizing: border-box;
  }

  .site-url {
    position: absolute; right: 31px; top: 705px;
    font-family: "Roboto Condensed", "Arial Narrow", sans-serif;
    font-weight: 700; font-size: 14px; color: #fff; line-height: 26px;
  }
</style>
</head>
<body>

<!-- Colour variant -->
<section class="page page--colour">
  <svg class="header-shapes" viewBox="0 0 523 48" aria-hidden="true">
    <polygon class="fill-dark" points="344,0 523,0 523,24 307,24"/>
    <polygon class="fill-accent" points="0,0 344,0 266,48 0,48"/>
  </svg>
  <div class="sidebar"></div>
  <div class="date-label">DATE:</div>
  <div class="date-field"></div>

  <div class="brand"><span class="brand-dot"></span><span class="brand-name">Brightpath</span></div>

  <div class="tab revision-tab">REVISION</div>
  <div class="box revision">
    <div class="revision-col">
      <div class="revision-row"><span class="num-cell">1</span></div>
      <div class="revision-row"><span class="num-cell">2</span></div>
      <div class="revision-row"><span class="num-cell">3</span></div>
      <div class="revision-row"><span class="num-cell">4</span></div>
    </div>
    <div class="revision-col">
      <div class="revision-row"><span class="num-cell">5</span></div>
      <div class="revision-row"><span class="num-cell">6</span></div>
      <div class="revision-row"><span class="num-cell">7</span></div>
      <div class="revision-row"><span class="num-cell">8</span></div>
    </div>
  </div>

  <div class="tab homework-tab">HOMEWORK</div>
  <div class="box homework">
    <div class="line-row">Subject:</div><div class="line-row">Task:</div>
    <div class="line-row">Subject:</div><div class="line-row">Task:</div>
    <div class="line-row">Subject:</div><div class="line-row">Task:</div>
    <div class="line-row">Subject:</div><div class="line-row">Subject:</div>
    <div class="line-row">Task:</div><div class="line-row">Subject:</div>
    <div class="line-row">Task:</div>
  </div>

  <div class="tab assess-tab">ASSESSMENTS</div>
  <div class="box assessments">
    <div class="assess-item"><div class="line-row">Assessment:<span class="due-label">Due</span></div><div class="line-row">Element:</div></div>
    <div class="assess-item"><div class="line-row">Assessment:<span class="due-label">Due</span></div><div class="line-row">Element:</div></div>
    <div class="assess-item"><div class="line-row">Assessment:<span class="due-label">Due</span></div><div class="line-row">Element:</div></div>
    <div class="assess-item"><div class="line-row">Assessment:<span class="due-label">Due</span></div><div class="line-row">Element:</div></div>
    <div class="assess-item"><div class="line-row">Assessment:<span class="due-label">Due</span></div><div class="line-row">Element:</div></div>
    <div class="assess-item"><div class="line-row">Assessment:<span class="due-label">Due</span></div><div class="line-row">Element:</div></div>
  </div>

  <div class="box lists">
    <div class="list">
      <div class="list-head">NOTES</div>
      <div class="list-body list-body--split">
        <div class="list-col">
          <div class="list-row"><span class="list-num">1</span></div><div class="list-row"><span class="list-num">2</span></div>
          <div class="list-row"><span class="list-num">3</span></div><div class="list-row"><span class="list-num">4</span></div>
        </div>
        <div class="list-col">
          <div class="list-row"><span class="list-num">5</span></div><div class="list-row"><span class="list-num">6</span></div>
          <div class="list-row"><span class="list-num">7</span></div><div class="list-row"><span class="list-num">8</span></div>
        </div>
      </div>
    </div>
    <div class="list">
      <div class="list-head">PRACTICE</div>
      <div class="list-body">
        <div class="list-col">
          <div class="list-row"><span class="list-num">1</span></div><div class="list-row"><span class="list-num">2</span></div>
          <div class="list-row"><span class="list-num">3</span></div><div class="list-row"><span class="list-num">4</span></div>
        </div>
      </div>
    </div>
  </div>

  <svg class="footer-shapes" viewBox="0 0 523 30" aria-hidden="true">
    <polygon class="fill-dark" points="250,0 264,0 312,30 298,30"/>
    <polygon class="fill-accent" points="264,0 523,0 523,30 312,30"/>
  </svg>
  <div class="site-url">www.brightpathstudy.com.au</div>
</section>

<!-- Mono variant -->
<section class="page page--mono">
  <svg class="header-shapes" viewBox="0 0 523 48" aria-hidden="true">
    <polygon class="fill-dark" points="344,0 523,0 523,24 307,24"/>
    <polygon class="fill-accent" points="0,0 344,0 266,48 0,48"/>
  </svg>
  <div class="sidebar"></div>
  <div class="date-label">DATE:</div>
  <div class="date-field"></div>

  <div class="brand"><span class="brand-dot"></span><span class="brand-name">Brightpath</span></div>

  <div class="tab revision-tab">REVISION</div>
  <div class="box revision">
    <div class="revision-col">
      <div class="revision-row"><span class="num-cell">1</span></div>
      <div class="revision-row"><span class="num-cell">2</span></div>
      <div class="revision-row"><span class="num-cell">3</span></div>
      <div class="revision-row"><span class="num-cell">4</span></div>
    </div>
    <div class="revision-col">
      <div class="revision-row"><span class="num-cell">5</span></div>
      <div class="revision-row"><span class="num-cell">6</span></div>
      <div class="revision-row"><span class="num-cell">7</span></div>
      <div class="revision-row"><span class="num-cell">8</span></div>
    </div>
  </div>

  <div class="tab homework-tab">HOMEWORK</div>
  <div class="box homework">
    <div class="line-row">Subject:</div><div class="line-row">Task:</div>
    <div class="line-row">Subject:</div><div class="line-row">Task:</div>
    <div class="line-row">Subject:</div><div class="line-row">Task:</div>
    <div class="line-row">Subject:</div><div class="line-row">Subject:</div>
    <div class="line-row">Task:</div><div class="line-row">Subject:</div>
    <div class="line-row">Task:</div>
  </div>

  <div class="tab assess-tab">ASSESSMENTS</div>
  <div class="box assessments">
    <div class="assess-item"><div class="line-row">Assessment:<span class="due-label">Due</span></div><div class="line-row">Element:</div></div>
    <div class="assess-item"><div class="line-row">Assessment:<span class="due-label">Due</span></div><div class="line-row">Element:</div></div>
    <div class="assess-item"><div class="line-row">Assessment:<span class="due-label">Due</span></div><div class="line-row">Element:</div></div>
    <div class="assess-item"><div class="line-row">Assessment:<span class="due-label">Due</span></div><div class="line-row">Element:</div></div>
    <div class="assess-item"><div class="line-row">Assessment:<span class="due-label">Due</span></div><div class="line-row">Element:</div></div>
    <div class="assess-item"><div class="line-row">Assessment:<span class="due-label">Due</span></div><div class="line-row">Element:</div></div>
  </div>

  <div class="box lists">
    <div class="list">
      <div class="list-head">NOTES</div>
      <div class="list-body list-body--split">
        <div class="list-col">
          <div class="list-row"><span class="list-num">1</span></div><div class="list-row"><span class="list-num">2</span></div>
          <div class="list-row"><span class="list-num">3</span></div><div class="list-row"><span class="list-num">4</span></div>
        </div>
        <div class="list-col">
          <div class="list-row"><span class="list-num">5</span></div><div class="list-row"><span class="list-num">6</span></div>
          <div class="list-row"><span class="list-num">7</span></div><div class="list-row"><span class="list-num">8</span></div>
        </div>
      </div>
    </div>
    <div class="list">
      <div class="list-head">PRACTICE</div>
      <div class="list-body">
        <div class="list-col">
          <div class="list-row"><span class="list-num">1</span></div><div class="list-row"><span class="list-num">2</span></div>
          <div class="list-row"><span class="list-num">3</span></div><div class="list-row"><span class="list-num">4</span></div>
        </div>
      </div>
    </div>
  </div>

  <svg class="footer-shapes" viewBox="0 0 523 30" aria-hidden="true">
    <polygon class="fill-dark" points="250,0 264,0 312,30 298,30"/>
    <polygon class="fill-accent" points="264,0 523,0 523,30 312,30"/>
  </svg>
  <div class="site-url">www.brightpathstudy.com.au</div>
</section>

</body>
</html>
```